The tide parlor saltwater aquarium store business card

Looking for a serious business card for a saltwater fish and coral store. I want this thing to blow people's minds when they see it. I would like the card to look very professional but I also want people to know what the tide parlor is just by seeing the card. Iam pretty open to anything as long as it's one of a kind.

Industry/Entity Type

Business

Contact Information for Business Card

31857 Dunmore highway Mardenburg pa 17428. Thetideparlor.example. Customerservice@thetideparlor.example. 5558204716

Requirements
Should not have
• Please no child like fish designs

```html
<!DOCTYPE html>
<html lang="en">
<head>
<meta charset="utf-8">
<title>The tide parlor – business card</title>
<link rel="stylesheet" href="https://fonts.googleapis.com/css2?family=Open+Sans:wght@400;600&display=swap">
<style>
  :root {
    --teal: #17859b;
    --teal-soft: #6fb4c2;
    --icon-fill: #8cc3cf;
    --card: #f4f5f5;
    --stage: #e4e6e7;
  }
  * { box-sizing: border-box; margin: 0; padding: 0; }
  html, body {
    width: 1200px; height: 1000px; overflow: hidden;
    background: var(--stage);
    font-family: "Open Sans", Arial, sans-serif;
    color: var(--teal);
  }
  .card {
    position: absolute;
    left: 250px;
    width: 700px; height: 400px;
    background: radial-gradient(ellipse at 55% 40%, #ffffff 0%, var(--card) 70%);
    box-shadow: 0 6px 18px rgba(0,0,0,0.18);
    overflow: hidden;
  }
  .card--front { top: 60px; }
  .card--back { top: 540px; }

  .brand { position: absolute; display: flex; align-items: center; }
  .brand__name {
    font-size: 46px; font-weight: 600; letter-spacing: 1px; line-height: 62px;
    color: var(--teal); white-space: nowrap;
  }
  .rule { position: absolute; height: 1px; background: var(--teal-soft); }
  .rule--bold { height: 3px; background: var(--teal); }

  /* front */
  .card--front .brand { left: 0; right: 0; top: 120px; justify-content: center; }
  .front__web {
    position: absolute; left: 0; right: 0; top: 244px;
    text-align: center; font-size: 19px; line-height: 28px;
    letter-spacing: 0.5px; color: var(--teal-soft);
  }

  /* back */
  .back__edge {
    position: absolute; left: 0; top: 100px; width: 6px; height: 150px; background: var(--teal);
  }
  .card--back .brand { left: 50px; top: 110px; }
  .contact { position: absolute; left: 230px; top: 222px; list-style: none; }
  .contact__item {
    display: flex; align-items: center; gap: 12px;
    font-size: 17px; line-height: 30px; margin-bottom: 12px; white-space: nowrap;
  }
  .contact__icon { width: 30px; height: 30px; flex: none; }
</style>
</head>
<body>

<section class="card card--front" aria-label="Business card front">
  <div class="rule" style="left:440px; width:100px; top:110px;"></div>
  <div class="brand"><span class="brand__name">The tide parlor</span></div>
  <div class="rule" style="left:200px; width:300px; top:212px;"></div>
  <p class="front__web">Thetideparlor.example</p>
  <div class="rule rule--bold" style="left:490px; width:210px; top:257px;"></div>
  <div class="rule rule--bold" style="left:0; width:210px; top:300px;"></div>
</section>

<section class="card card--back" aria-label="Business card back">
  <div class="back__edge"></div>
  <div class="rule" style="left:300px; width:90px; top:100px;"></div>
  <div class="brand"><span class="brand__name">The tide parlor</span></div>
  <div class="rule" style="left:60px; width:240px; top:186px;"></div>

  <ul class="contact">
    <li class="contact__item">
      <svg class="contact__icon" viewBox="0 0 30 30" aria-hidden="true">
        <circle cx="15" cy="15" r="14" fill="var(--icon-fill)" stroke="var(--teal)" stroke-width="1"/>
        <rect x="10.5" y="7" width="9" height="16" rx="1.5" fill="#fff"/>
        <rect x="12" y="9" width="6" height="9" fill="var(--icon-fill)"/>
      </svg>
      <span>5558204716</span>
    </li>
    <li class="contact__item">
      <svg class="contact__icon" viewBox="0 0 30 30" aria-hidden="true">
        <circle cx="15" cy="15" r="14" fill="var(--icon-fill)" stroke="var(--teal)" stroke-width="1"/>
        <rect x="8" y="10" width="14" height="10" fill="#fff"/>
        <path d="M8 10 L15 16 L22 10" fill="none" stroke="var(--icon-fill)" stroke-width="1.4"/>
      </svg>
      <span>Customerservice@thetideparlor.example</span>
    </li>
    <li class="contact__item">
      <svg class="contact__icon" viewBox="0 0 30 30" aria-hidden="true">
        <circle cx="15" cy="15" r="14" fill="var(--icon-fill)" stroke="var(--teal)" stroke-width="1"/>
        <path d="M15 23 C11 18 10 15.5 10 13 a5 5 0 0 1 10 0 c0 2.5 -1 5 -5 10z" fill="#fff"/>
        <circle cx="15" cy="13" r="2" fill="var(--icon-fill)"/>
      </svg>
      <span>31857 Dunmore highway Mardenburg pa 17428</span>
    </li>
  </ul>
</section>

</body>
</html>
```